cosmetics need shampoo label of first product (hopefully many more to follow)

we are starting this new project with the creation of the first of a range of shampoos: Design of facing comprehend creation of logo and facing of the product, we want to achieve a brand recognition and facing that makes our product and product stand out, see briefing attached.

We want to have a degree of personality but also give a tone of professional brand.

If project takes off, then more product to design and more resources available.

Target Market(s)

consumer looking for a professional shampoo but not at hairdresser at convenient price and size (1 litre with pump) bottle of white plastic

Industry/Entity Type

Cosmetics

Colors
00a990

Requirements
Must have
• as this shampoo is for damaged hair, green colour is the one that symbolise this category see Voluméa Brillance
• we want that the bottle stand out from the crowd and that people get that is a professional brand so the logo velNura must be seen and the colour most make a difference in the shelves
Nice to have
• good balance between some personality and & professional
• not too white (as will not stand out in white products shelve) but not too colour as they may then merchandise in the shelve with coloured product
• big fonts easy to read
Should not have
• too clinical, to boring,

```html
<!DOCTYPE html>
<html lang="en">
<head>
<meta charset="utf-8">
<title>velNura Repair Shampoo Label</title>
<link rel="stylesheet" href="https://fonts.googleapis.com/css2?family=Comfortaa:wght@400;500;700&family=Roboto+Condensed:wght@500&family=Montserrat:wght@500&display=swap">
<style>
  :root {
    --teal: #00a990;
    --teal-dark: #006b5a;
    --teal-ink: #0d6b5c;
    --teal-text: #0e5e52;
    --mint-light: #d7f7ea;
    --mint: #a6e6cf;
    --grey: #a9a9a9;
    --white: #ffffff;
    --black: #111111;
  }
  * { margin: 0; padding: 0; box-sizing: border-box; }
  html, body { width: 1200px; height: 2326px; overflow: hidden; background: var(--white); }
  .label { position: relative; width: 1200px; height: 2326px; background: var(--white); }

  .brand-name {
    position: absolute; top: 150px; left: 0; width: 1200px; text-align: center;
    font-family: "Comfortaa", sans-serif; font-weight: 500; font-size: 230px;
    line-height: 1; color: var(--teal); letter-spacing: -4px;
  }
  .brand-tagline {
    position: absolute; top: 490px; left: 0; width: 1200px; text-align: center;
    font-family: "Roboto Condensed", sans-serif; font-weight: 500; font-size: 68px;
    color: var(--grey);
  }

  .top-band { position: absolute; top: 746px; left: 0; width: 1200px; height: 48px; background: var(--teal-dark); }
  .top-rule { position: absolute; top: 803px; left: 0; width: 1200px; height: 5px; background: var(--teal-dark); }

  .name-panel {
    position: absolute; top: 812px; left: 0; width: 1200px; height: 650px;
    background:
      radial-gradient(ellipse 500px 260px at 800px 120px, rgba(255,255,255,0.75), transparent 70%),
      radial-gradient(ellipse 520px 200px at 1000px 560px, rgba(120,230,200,0.55), transparent 70%),
      radial-gradient(ellipse 600px 240px at 200px 330px, rgba(255,255,255,0.45), transparent 70%),
      linear-gradient(170deg, var(--mint) 0%, var(--mint-light) 45%, var(--mint) 100%);
  }
  .bottom-rule { position: absolute; top: 1466px; left: 0; width: 1200px; height: 5px; background: var(--teal-dark); }

  .product-name-en {
    position: absolute; left: 140px; top: 838px;
    font-family: "Comfortaa", sans-serif; font-weight: 500; font-size: 74px; line-height: 96px;
    color: var(--teal-ink);
  }
  .product-name-fr {
    position: absolute; left: 130px; top: 1140px;
    font-family: "Comfortaa", sans-serif; font-weight: 400; font-size: 76px; line-height: 92px;
    color: var(--teal-text);
  }

  .hair-type-band {
    position: absolute; top: 1479px; left: 0; width: 1200px; height: 217px; background: var(--teal);
    padding-top: 46px; text-align: center;
    font-family: "Comfortaa", sans-serif; font-weight: 500; font-size: 46px; line-height: 72px;
    color: var(--white);
  }

  .claims-pill {
    position: absolute; top: 2021px; left: 128px; width: 944px; height: 73px;
    border-radius: 37px; background: var(--grey);
    display: flex; align-items: center; justify-content: center;
    font-family: "Comfortaa", sans-serif; font-weight: 700; font-size: 40px;
    color: var(--white);
  }

  .net-weight {
    position: absolute; top: 2198px; left: 0; width: 1200px; text-align: center;
    font-family: "Montserrat", sans-serif; font-weight: 500; font-size: 38px;
    color: var(--black);
  }
</style>
</head>
<body>
  <main class="label">
    <div class="brand-name">velNura</div>
    <div class="brand-tagline">salon formula</div>

    <div class="top-band"></div>
    <div class="top-rule"></div>
    <section class="name-panel"></section>
    <div class="bottom-rule"></div>

    <h1 class="product-name-en">Repair shampoo<br>With argan oil</h1>
    <p class="product-name-fr">Shampooing<br>reparateur avec huile<br>argain</p>

    <section class="hair-type-band">
      <p>For weakened – damaged hair</p>
      <p>Pour cheveux habimes et affaiblis</p>
    </section>

    <div class="claims-pill">Parabens free – sls free – colour safe</div>

    <p class="net-weight">NET WT 33.8 fl oz e 1000 ml</p>
  </main>
</body>
</html>
```